The Velvet Magpie business card

I need a business card for my makeup artist business. I specialise in bridal, glamour, formal and special occasion makeup.
I am a mobile makeup artist who caters for every from nowra to sydney.
I do the following services:
Bridal makeup
airbrush makeup
special occasion
formals
hens nights/ girls night
makeup lesson
makeup for all ages from flower girl to Nanna of the bride!
photoshoot makeup
SPFX

I would like the card to portray a very professional sleek makeup business. I would also like another version of the card directed especially towards brides.

Please see my website to understand colours etc www.thevelvetmagpie.com

The Velvet Magpie
Professional Makeup Artist
Marisol Dunkel
0471829304
info@thevelvetmagpie.com
www.thevelvetmagpie.com
www.facebook.com/thevelvetmagpie

```html
<!DOCTYPE html>
<html lang="en">
<head>
<meta charset="utf-8">
<title>The Velvet Magpie – Business Card</title>
<link rel="stylesheet" href="https://fonts.googleapis.com/css2?family=Oswald:wght@300;400;500&family=Open+Sans:wght@700&display=swap">
<style>
  :root {
    --backdrop: #ececec;
    --card-white: #ffffff;
    --magenta: #e0198a;
    --magenta-deep: #c8107a;
    --magenta-light: #f03aa0;
    --charcoal: #3a3a3a;
    --grey-dark: #5a5a5a;
    --grey-mid: #9c9c9c;
    --grey-faint: #e4e4e4;
    --text-dark: #2e2e2e;
    --text-light: #ffffff;
  }
  * { margin: 0; padding: 0; box-sizing: border-box; }
  html, body {
    width: 1200px; height: 913px; overflow: hidden;
    background: var(--backdrop);
  }
  .canvas { position: relative; width: 1200px; height: 913px; }

  .card {
    position: absolute; width: 580px; height: 330px;
    border-radius: 16px; overflow: hidden;
    box-shadow: 0 10px 30px rgba(0,0,0,0.18);
  }
  .card-front { left: 50px; top: 120px; background: var(--card-white); }
  .card-back  { left: 570px; top: 463px; background: linear-gradient(160deg, var(--magenta-light), var(--magenta) 45%, var(--magenta-deep)); }

  .card-art { position: absolute; inset: 0; width: 100%; height: 100%; }

  .brand-name {
    position: absolute; left: 40px; top: 88px;
    font-family: "Oswald", sans-serif; font-weight: 400;
    font-size: 46px; letter-spacing: 2px; text-transform: uppercase;
    color: var(--magenta); line-height: 1;
  }

  .contact-list {
    position: absolute; left: 58px; top: 176px;
    list-style: none;
    font-family: "Oswald", sans-serif; font-weight: 400;
    font-size: 17px; color: var(--text-dark);
  }
  .contact-item { display: flex; align-items: center; height: 26px; }
  .contact-icon { width: 16px; height: 16px; margin-right: 10px; flex: none; }

  .artist {
    position: absolute; left: 420px; top: 192px;
    color: var(--text-light);
  }
  .artist-name {
    font-family: "Open Sans", sans-serif; font-weight: 700;
    font-size: 19px; line-height: 1.2;
  }
  .artist-role {
    font-family: "Oswald", sans-serif; font-weight: 300;
    font-size: 15px; letter-spacing: 0.3px;
  }

  .services {
    position: absolute; left: 20px; right: 20px; top: 232px;
    font-family: "Oswald", sans-serif; font-weight: 400;
    font-size: 15.5px; line-height: 1.55; text-align: center;
    color: var(--text-light);
  }
</style>
</head>
<body>
<main class="canvas">

  <section class="card card-front" aria-label="Card front">
    <svg class="card-art" viewBox="0 0 580 330" aria-hidden="false">
      <defs>
        <radialGradient id="swirl-tone" cx="0.5" cy="0.5" r="0.5">
          <stop offset="0" stop-color="#d8d8d8"/>
          <stop offset="1" stop-color="#f4f4f4" stop-opacity="0"/>
        </radialGradient>
        <linearGradient id="magenta-sweep" x1="0" y1="0" x2="1" y2="1">
          <stop offset="0" stop-color="#f03aa0"/>
          <stop offset="1" stop-color="#c8107a"/>
        </linearGradient>
      </defs>
      <g role="img" aria-label="Faint swirl ornament">
        <ellipse cx="510" cy="40" rx="95" ry="55" fill="url(#swirl-tone)"/>
      </g>
      <path d="M580,50 C500,80 440,130 405,190 C370,255 300,315 190,330 L580,330 Z" fill="url(#magenta-sweep)"/>
      <path d="M578,36 C492,72 426,126 390,188 C354,252 286,306 160,326" fill="none" stroke="var(--grey-dark)" stroke-width="9" stroke-linecap="round"/>
      <path d="M572,22 C480,62 410,118 374,182 C338,246 270,298 130,318" fill="none" stroke="var(--grey-mid)" stroke-width="4" stroke-linecap="round"/>
    </svg>

    <div class="brand-name">The Velvet Magpie</div>

    <ul class="contact-list">
      <li class="contact-item">
        <svg class="contact-icon" viewBox="0 0 16 16"><path d="M2 6c0-2 2-3 6-3s6 1 6 3v1h-3V5.5H5V7H2z M3 8h10l1 5H2z" fill="var(--magenta)"/><circle cx="8" cy="10.5" r="1.6" fill="#fff"/></svg>
        0471829304
      </li>
      <li class="contact-item">
        <svg class="contact-icon" viewBox="0 0 16 16"><rect x="1" y="3" width="14" height="10" fill="var(--magenta)"/><path d="M1 3l7 6 7-6" fill="none" stroke="#fff" stroke-width="1.4"/></svg>
        info@thevelvetmagpie.com
      </li>
      <li class="contact-item">
        <svg class="contact-icon" viewBox="0 0 16 16"><circle cx="8" cy="8" r="7" fill="var(--magenta)"/><path d="M1 8h14M8 1v14M3 4.5h10M3 11.5h10" stroke="#fff" stroke-width="1"/><ellipse cx="8" cy="8" rx="3" ry="7" fill="none" stroke="#fff" stroke-width="1"/></svg>
        www.thevelvetmagpie.com
      </li>
      <li class="contact-item">
        <svg class="contact-icon" viewBox="0 0 16 16"><rect x="1" y="1" width="14" height="14" fill="var(--magenta)"/></svg>
        /thevelvetmagpie
      </li>
    </ul>

    <div class="artist">
      <div class="artist-name">Marisol Dunkel</div>
      <div class="artist-role">Professional Makeup Artist</div>
    </div>
  </section>

  <section class="card card-back" aria-label="Card back">
    <svg class="card-art" viewBox="0 0 580 330">
      <defs>
        <linearGradient id="tone-party" x1="0" y1="0" x2="0" y2="1">
          <stop offset="0" stop-color="#3a3030"/><stop offset="1" stop-color="#2b2f78"/>
        </linearGradient>
        <linearGradient id="tone-lashes" x1="0" y1="0" x2="1" y2="1">
          <stop offset="0" stop-color="#c9c3a0"/><stop offset="1" stop-color="#e2b9a4"/>
        </linearGradient>
        <linearGradient id="tone-bridesmaids" x1="0" y1="0" x2="0" y2="1">
          <stop offset="0" stop-color="#cfc8b8"/><stop offset="1" stop-color="#2c3170"/>
        </linearGradient>
        <linearGradient id="tone-closeup" x1="0" y1="0" x2="1" y2="1">
          <stop offset="0" stop-color="#b9a27a"/><stop offset="1" stop-color="#f0d4c6"/>
        </linearGradient>
      </defs>
      <rect x="18" y="18" width="544" height="199" fill="#ffffff"/>
      <g role="img" aria-label="Photo of two bridesmaids in navy dresses holding a white bouquet">
        <polygon points="20,20 170,20 130,215 20,215" fill="url(#tone-party)"/>
      </g>
      <g role="img" aria-label="Photo of mascara being applied in close-up">
        <polygon points="176,20 320,20 280,215 136,215" fill="url(#tone-lashes)"/>
      </g>
      <g role="img" aria-label="Photo of two smiling bridesmaids with styled hair">
        <polygon points="326,20 460,20 420,215 286,215" fill="url(#tone-bridesmaids)"/>
      </g>
      <g role="img" aria-label="Photo of lipstick being applied to a bride">
        <polygon points="466,20 560,20 560,215 426,215" fill="url(#tone-closeup)"/>
      </g>
    </svg>

    <p class="services">
      Bridal makeup • Airbrush makeup • Special occasion • Formals<br>
      • Hens nights/ Girls night • Makeup lesson • Makeup for all ages from flower<br>
      girl to Nanna of the bride! • Photoshoot makeup • SPFX
    </p>
  </section>

</main>
</body>
</html>
```